Business Cards for company that supports physicians that do medical research

Need to create a business card for Aldren Studies (www.aldrenstudies.example), a company devoted to supporting physicians who conduct medical research. The form of the card should match the message of research and information quest. I have provided the logo of the company as an uploaded file. Designs should be simple and slick aimed at very high end clients.

Target Market(s)

Medical doctors that are also researchers

Industry/Entity Type

Medical

Contact Information for Business Card

Should feature logo and fields for personal info:
Name/title
Phone /email

Font styles to use
Serif
Sans Serif

Requirements
Must have
• Aldren logo and fields for personal info:
• Name: Corwin Abbatelli
• Title: VP Research and Senior Analyst
• Phone: 555-203-7416
• email: info@aldrenstudies.example
Nice to have
• Interesting cards that I've seen:
• 1- all black/charcoal or very dark background
• 2- Plastic - semi-transparent
• 3- non-standard height-width ratios
• 4- Functional cards -- USB drive incorporated
Should not have
• Too busy; needs to stay very simple

```html
<!DOCTYPE html>
<html lang="en">
<head>
<meta charset="utf-8">
<title>Aldren Studies – Business Card</title>
<link rel="stylesheet" href="https://fonts.googleapis.com/css2?family=Lato:wght@400;700&display=swap">
<style>
  :root {
    --page-bg: #e9e9e9;
    --card-bg: #ffffff;
    --brand-blue: #1a82c8;
    --brand-green: #5cb531;
    --text-dark: #2b2b2b;
    --divider: rgba(0,0,0,0.12);
  }
  * { margin: 0; padding: 0; box-sizing: border-box; }
  html, body {
    width: 1200px; height: 898px; overflow: hidden;
    background: var(--page-bg);
    font-family: "Lato", Arial, sans-serif;
  }
  .canvas {
    width: 1200px; height: 898px;
    display: flex; align-items: center; justify-content: center;
  }
  .business-card {
    position: relative;
    width: 840px; height: 480px;
    background: var(--card-bg);
    box-shadow: 0 10px 30px rgba(0,0,0,0.15);
    overflow: hidden;
  }
  .divider {
    position: absolute; left: 418px; top: 0;
    width: 2px; height: 330px;
    background: linear-gradient(to bottom, var(--divider), var(--divider) 70%, transparent);
  }
  .brand {
    position: absolute; left: 70px; top: 236px;
    display: flex; align-items: center; gap: 14px;
  }
  .brand-dot {
    width: 30px; height: 30px; border-radius: 50%;
    background: var(--brand-blue);
  }
  .brand-name {
    font-size: 36px; font-weight: 700; color: var(--brand-green);
    letter-spacing: 0.5px; white-space: nowrap;
  }
  .name-tab {
    position: absolute; left: 420px; top: 60px;
    width: 380px; height: 88px;
    background: var(--brand-blue);
    border-radius: 0 10px 10px 0;
    padding: 13px 0 0 50px;
    color: #fff;
    box-shadow: 0 4px 8px rgba(0,0,0,0.15);
  }
  .person-name { font-size: 24px; font-weight: 400; line-height: 1.1; white-space: nowrap; }
  .person-name strong { font-weight: 700; }
  .person-title { font-size: 15px; line-height: 1.15; margin-top: 4px; padding-left: 6px; }
  .contact-list {
    position: absolute; left: 470px; top: 180px;
    list-style: none;
    font-size: 19px; color: var(--text-dark);
  }
  .contact-list li { display: flex; align-items: center; gap: 16px; margin-bottom: 12px; white-space: nowrap; }
  .contact-list svg { width: 18px; height: 18px; fill: var(--text-dark); }
</style>
</head>
<body>
<main class="canvas">
  <section class="business-card">
    <div class="brand">
      <span class="brand-dot"></span>
      <span class="brand-name">Aldren Studies</span>
    </div>
    <div class="divider"></div>
    <div class="name-tab">
      <p class="person-name">Corwin <strong>Abbatelli</strong></p>
      <p class="person-title">VP Research<br>and Senior Analyst</p>
    </div>
    <ul class="contact-list">
      <li>
        <svg viewBox="0 0 24 24" aria-hidden="true"><path d="M3 9c0-3 4-5 9-5s9 2 9 5v2h-5V9H8v2H3z"/><path d="M6 12h12l2 8H4z"/><circle cx="12" cy="16" r="2" fill="#fff"/></svg>
        <span>555-203-7416</span>
      </li>
      <li>
        <svg viewBox="0 0 24 24" aria-hidden="true"><path d="M2 5h20v14H2z"/><path d="M2 5l10 8 10-8" fill="none" stroke="#fff" stroke-width="1.8"/></svg>
        <span>info@aldrenstudies.example</span>
      </li>
    </ul>
  </section>
</main>
</body>
</html>
```